Business Card Design

We need a business card design for a Dry cleaners in Brisbane, Australia. We are trying to promote a fresh/clean image consistent with our website. www.quillpresswash.com.au

Looking for a professional neat card that's easy to read.

Target Market(s)

Customers looking for a professional, fresh and clean drycleaners.

Industry/Entity Type

Business

Contact Information for Business Card

See our existing business card. The Fax number (07) 3468 5203 to be removed.

Requirements
Must have
• All the details on current business card less the fax number.
Nice to have
• I like white text on coloured background. Blue works well as we are located near the water...

```html
<!DOCTYPE html>
<html lang="en">
<head>
<meta charset="utf-8">
<title>Quill Press Wash – Business Card Concepts</title>
<link href="https://fonts.googleapis.com/css2?family=Jost:wght@400;500&family=Oswald:wght@300;400&display=swap" rel="stylesheet">
<style>
  :root {
    --bay-blue: #2a3a8e;
    --white: #ffffff;
    --page: #ffffff;
  }
  html, body {
    margin: 0;
    padding: 0;
    width: 1200px;
    height: 1000px;
    overflow: hidden;
    background: var(--page);
  }
  .canvas {
    position: relative;
    width: 1200px;
    height: 1000px;
  }
  .card {
    position: absolute;
    left: 291px;
    width: 622px;
    height: 376px;
    background: var(--bay-blue);
    overflow: hidden;
    font-family: "Jost", sans-serif;
    color: var(--white);
  }
  .card--straight { top: 79px; }
  .card--wave { top: 524px; }

  .brand-name {
    position: absolute;
    left: 70px;
    width: 215px;
    top: 153px;
    font-family: "Jost", sans-serif;
    font-weight: 500;
    font-size: 25px;
    letter-spacing: 0.5px;
    color: var(--white);
    display: flex;
    align-items: center;
    justify-content: center;
    gap: 10px;
  }
  .brand-name .brand-dot {
    width: 10px;
    height: 10px;
    border-radius: 50%;
    background: var(--white);
    flex: none;
  }

  .locations-band {
    position: absolute;
    left: 0;
    top: 236px;
    height: 26px;
    background: var(--white);
    color: var(--bay-blue);
    font-family: "Oswald", sans-serif;
    font-weight: 400;
    font-size: 15px;
    line-height: 26px;
    white-space: nowrap;
  }
  .locations-band .locations {
    position: absolute;
    left: 0;
    width: 348px;
    text-align: center;
  }
  .card--straight .locations-band { width: 315px; }
  .card--wave .locations-band { width: 290px; }

  .name-band {
    position: absolute;
    right: 0;
    top: 95px;
    height: 25px;
    background: var(--white);
    color: var(--bay-blue);
    font-family: "Oswald", sans-serif;
    font-weight: 400;
    font-size: 21px;
    line-height: 25px;
    text-transform: uppercase;
    white-space: nowrap;
  }
  .card--straight .name-band { left: 315px; padding-left: 37px; }
  .card--wave .name-band { left: 337px; padding-left: 15px; }

  .divider {
    position: absolute;
    left: 315px;
    top: 60px;
    width: 1px;
    height: 257px;
    background: var(--white);
  }
  .wave {
    position: absolute;
    left: 0;
    top: 0;
  }

  .contact {
    position: absolute;
    left: 352px;
    margin: 0;
    font-size: 14.5px;
    line-height: 19.5px;
    letter-spacing: 0.3px;
    white-space: nowrap;
  }
  .contact-lines { top: 145px; }
  .contact-address { top: 242px; }
  .contact .label { display: inline-block; width: 12px; }
</style>
</head>
<body>
<div class="canvas">

  <section class="card card--straight" aria-label="Business card, straight divider">
    <div class="brand-name"><span class="brand-dot"></span>Quill Press Wash</div>
    <div class="locations-band"><span class="locations">Kelpbay · Harbourvale · Saltmarsh Pt</span></div>
    <div class="divider"></div>
    <div class="name-band">Morgan Tellis</div>
    <p class="contact contact-lines">
      <span class="label">M</span> 0412 586 307<br>
      <span class="label">E</span> morgan@quillpresswash.com<br>
      <span class="label">P</span> (07) 3520 4416
    </p>
    <p class="contact contact-address">
      18 Shorebird St<br>
      Kelpbay Qld 4191
    </p>
  </section>

  <section class="card card--wave" aria-label="Business card, wave divider">
    <div class="brand-name"><span class="brand-dot"></span>Quill Press Wash</div>
    <div class="locations-band"><span class="locations">Kelpbay · Harbourvale · Saltmarsh Pt</span></div>
    <svg class="wave" width="622" height="376" viewBox="0 0 622 376" aria-hidden="true">
      <path fill="#ffffff" d="M331,43 C349,76 344,111 329,141 L299,221 C289,251 289,276 297,304 C284,281 277,256 284,226 L314,141 C329,106 337,76 331,43 Z"/>
    </svg>
    <div class="name-band">Morgan Tellis</div>
    <p class="contact contact-lines">
      <span class="label">M</span> 0412 586 307<br>
      <span class="label">E</span> morgan@quillpresswash.com<br>
      <span class="label">P</span> (07) 3520 4416
    </p>
    <p class="contact contact-address">
      18 Shorebird St<br>
      Kelpbay Qld 4191
    </p>
  </section>

</div>
</body>
</html>
```